Harborline Motors LLC

Car Dealer Customer Service
Address: 2741 Linden Avenue, Shelbyville, TN 37162
web: www.harborlinemotorstn.net
email: harborlinemotorstn@mailbox-example.net
Phone: (931) 555-0148
Phone: (629) 555-0173

```html
<!DOCTYPE html>
<html lang="en">
<head>
<meta charset="utf-8">
<title>Harborline Motors — Business Card</title>
<link rel="stylesheet" href="https://fonts.googleapis.com/css2?family=Montserrat:wght@700;800&family=Inter:wght@400;500&display=swap">
<style>
  :root {
    --bg: #1d1d1f;
    --brand-blue: #2387c0;
    --deep-blue: #1a74aa;
    --navy: #0b3aa0;
    --sky: #33c3f0;
    --orange: #e9741a;
    --amber: #f5a93c;
    --sun: #f7dd6a;
    --paper: #f6f7f8;
    --ink: #3a3d42;
    --beige: #f3e7d6;
    --white: #ffffff;
  }
  * { margin: 0; padding: 0; box-sizing: border-box; }
  html, body { width: 1200px; height: 800px; overflow: hidden; }
  body {
    background: var(--bg);
    font-family: "Inter", Arial, sans-serif;
    display: flex;
    align-items: center;
    justify-content: center;
    gap: 60px;
  }
  .card {
    position: relative;
    width: 500px;
    height: 286px;
    border-radius: 18px;
    overflow: hidden;
  }

  /* Front */
  .card--front { background: var(--brand-blue); }
  .front-art {
    position: absolute;
    left: 0; bottom: 0;
    width: 340px; height: 230px;
    border-top-right-radius: 140px;
    background:
      linear-gradient(180deg, transparent 0 48%, rgba(0,0,0,0) 48%),
      linear-gradient(100deg, var(--sun) 0%, var(--amber) 40%, var(--orange) 100%);
    overflow: hidden;
  }
  .front-art::before {
    content: "";
    position: absolute;
    left: 0; top: 0;
    width: 100%; height: 48%;
    background: linear-gradient(100deg, var(--sky) 0%, #1f6fd0 45%, var(--navy) 100%);
  }
  .front-brand {
    position: absolute;
    right: 34px; top: 54px;
    text-align: right;
    color: var(--white);
  }
  .front-brand__name {
    font-family: "Montserrat", Arial, sans-serif;
    font-weight: 800;
    font-size: 26px;
    letter-spacing: 0.5px;
    line-height: 1;
  }
  .front-brand__web {
    margin-top: 6px;
    font-size: 10.5px;
    letter-spacing: 3px;
  }

  /* Back */
  .card--back { background: var(--paper); }
  .back-band {
    position: absolute;
    top: 0; right: 0;
    width: 330px; height: 150px;
  }
  .back-faint-art {
    position: absolute;
    right: 0; bottom: 0;
    width: 250px; height: 150px;
    border-top-left-radius: 90px;
    background: linear-gradient(120deg, var(--beige) 0%, #f6ede2 100%);
  }
  .person {
    position: absolute;
    right: 30px; top: 34px;
    text-align: right;
    color: var(--white);
  }
  .person__name {
    font-family: "Montserrat", Arial, sans-serif;
    font-weight: 700;
    font-size: 19px;
    letter-spacing: 0.4px;
  }
  .person__role { font-size: 11.5px; margin-top: 2px; }

  .identity {
    position: absolute;
    left: 40px; top: 40px;
  }
  .identity__mark {
    width: 54px; height: 54px;
    border-radius: 50%;
    background: var(--deep-blue);
    margin-bottom: 12px;
  }
  .identity__name {
    font-family: "Montserrat", Arial, sans-serif;
    font-weight: 800;
    font-size: 20px;
    color: var(--deep-blue);
    line-height: 1;
  }
  .address {
    margin-top: 10px;
    font-size: 11.5px;
    line-height: 1.4;
    color: var(--ink);
  }
  .contacts {
    list-style: none;
    margin-top: 10px;
    font-size: 11px;
    line-height: 1.5;
    color: var(--ink);
  }
  .contacts li { display: flex; align-items: center; gap: 7px; }
  .contacts svg { width: 10px; height: 10px; fill: var(--amber); flex: none; }
</style>
</head>
<body>

<section class="card card--front" aria-label="Business card front">
  <div class="front-art" role="img" aria-label="Brand illustration area in blue and orange tones"></div>
  <div class="front-brand">
    <div class="front-brand__name">HARBORLINE MOTORS</div>
    <div class="front-brand__web">www.harborlinemotorstn.net</div>
  </div>
</section>

<section class="card card--back" aria-label="Business card back">
  <svg class="back-band" viewBox="0 0 330 150" aria-hidden="true">
    <path d="M0 0 H330 V120 Q250 150 160 118 Q80 90 40 40 Q20 15 0 0 Z" fill="var(--deep-blue)"/>
  </svg>
  <div class="back-faint-art" role="img" aria-label="Faint brand illustration area in soft beige"></div>

  <div class="person">
    <div class="person__name">DANIEL WHITFORD</div>
    <div class="person__role">Founder &amp; CEO</div>
  </div>

  <div class="identity">
    <div class="identity__mark"></div>
    <div class="identity__name">HARBORLINE MOTORS</div>
    <p class="address">Car Dealer Customer Service<br>2741 Linden Avenue<br>Shelbyville, TN 37162</p>
    <ul class="contacts">
      <li><svg viewBox="0 0 10 10"><path d="M2 0.5 L3.6 2.6 L2.8 3.6 Q4 6 6.4 7.2 L7.4 6.4 L9.5 8 L8.4 9.5 Q1 8.5 0.5 1.6 Z"/></svg>(931) 555-0148</li>
      <li><svg viewBox="0 0 10 10"><path d="M2 0.5 L3.6 2.6 L2.8 3.6 Q4 6 6.4 7.2 L7.4 6.4 L9.5 8 L8.4 9.5 Q1 8.5 0.5 1.6 Z"/></svg>(629) 555-0173</li>
      <li><svg viewBox="0 0 10 10"><path d="M0 2 H10 V8.5 H0 Z M0.6 2.3 L5 5.6 L9.4 2.3" stroke="#fff" stroke-width="0.8"/></svg>harborlinemotorstn@mailbox-example.net</li>
      <li><svg viewBox="0 0 10 10"><circle cx="5" cy="5" r="4.6"/><path d="M0.6 5 H9.4 M5 0.4 Q2.4 5 5 9.6 M5 0.4 Q7.6 5 5 9.6" stroke="#fff" stroke-width="0.7" fill="none"/></svg>www.harborlinemotorstn.net</li>
    </ul>
  </div>
</section>

</body>
</html>
```